We need to have 2 different retractable banners designed that will be used at a variety of events. We plan to have the banners printed through printbriskly.example. According to their site, specs are as follows: Retractable banners are digitally printed on 12oz double-sided smooth vinyl. While the area on the retractable banners is 33 x 78, the customer will want to provide a file that has an area of 35 x 82 to account for bleed, with 3" of that vertical bleed at the bottom of the design. Recommneded DPI is 150. Upload capacity for retractable banners is 100MP.

Banner #1: Cascadia Labor Alliance logo at top; then the following text placed lower on the banner: Providing leadership that promotes and advances Oregon's workforce system. At the bottom of banner: cascadialabor alliance.example

Banner #2: Cascadia Labor Alliance logo at top; then the following text placed lower on the banner: Oregon's workforce system ensures all Oregonians possess the talent needed for communities to thrive and prosper. At the bottom of banner: cascadialaboralliance.example

Color scheme: complimentary colors of the Cascadia Labor Alliance logo.
Images: images representative of Oregon (for example: map of Oregon, Douglas fir trees, coastal range, etc.

I've attached a couple of previous banners created as a reference.

```html
<!DOCTYPE html>
<html lang="en">
<head>
<meta charset="utf-8">
<title>Cascadia Labor Alliance – Retractable Banners</title>
<link rel="stylesheet" href="https://fonts.googleapis.com/css2?family=Montserrat:wght@500;700;800&family=Roboto:wght@400&family=Cinzel:wght@500&display=swap">
<style>
  :root{
    --bg:#9db4cb;
    --navy:#0b2d6e;
    --magenta:#990057;
    --magenta-dark:#7d0047;
    --navy-dark:#082459;
    --paper:#f1f1f3;
    --white:#ffffff;
    --sea:#3fc6dc;
    --sea-deep:#1f8fb0;
    --cliff:#8a8a78;
    --fir:#4f7a2e;
    --fir-dark:#2d4f1c;
  }
  *{margin:0;padding:0;box-sizing:border-box}
  html,body{width:1200px;height:1200px;overflow:hidden;background:var(--bg)}
  .canvas{position:relative;width:1200px;height:1200px}
  .banner{position:absolute;top:103px;width:420px;height:994px;background:var(--paper);overflow:hidden}
  .banner--talent{left:150px}
  .banner--leadership{left:630px}
  .banner svg.shapes{position:absolute;left:0;top:0}
  .brand{position:absolute;left:0;width:100%;text-align:center}
  .brand__mark{width:62px;height:62px;margin:0 auto 14px;background:var(--navy)}
  .brand__name{font-family:"Cinzel",serif;font-weight:500;color:var(--navy);font-size:15px;letter-spacing:2px;line-height:1.35}
  .message{position:absolute;left:0;width:100%;text-align:center;color:var(--white);font-family:"Montserrat",sans-serif}
  .kicker{display:flex;align-items:center;justify-content:center;gap:6px;font-weight:500;font-size:14px}
  .kicker::before,.kicker::after{content:"";display:block;height:1.5px;background:var(--white)}
  .headline{font-weight:800;line-height:1}
  .subline{font-weight:800;line-height:1.25}
  .tagband{font-weight:500;font-size:12.5px;padding:5px 0}
  .url{position:absolute;left:0;width:100%;display:flex;align-items:center;gap:8px;font-family:"Roboto",sans-serif;font-size:16px;color:var(--white)}
  .url::before,.url::after{content:"";flex:1;height:2px}
  .banner--talent .url::before,.banner--talent .url::after{background:var(--navy)}
  .banner--leadership .url::before,.banner--leadership .url::after{background:var(--magenta)}
  .banner--talent .kicker::before,.banner--talent .kicker::after{width:34px}
  .banner--leadership .kicker{font-size:22px;letter-spacing:3px;gap:10px}
  .banner--leadership .kicker::before,.banner--leadership .kicker::after{width:70px}
</style>
</head>
<body>
<div class="canvas">

  <!-- Banner: talent message -->
  <section class="banner banner--talent">
    <svg class="shapes" width="420" height="994" viewBox="0 0 420 994">
      <defs>
        <linearGradient id="coastTone" x1="0" y1="0" x2="0" y2="1">
          <stop offset="0" stop-color="#c9d8e4"/>
          <stop offset="0.12" stop-color="#6f9cc2"/>
          <stop offset="0.3" stop-color="var(--cliff)"/>
          <stop offset="0.45" stop-color="#6e8a4a"/>
          <stop offset="0.62" stop-color="var(--sea)"/>
          <stop offset="1" stop-color="var(--sea-deep)"/>
        </linearGradient>
      </defs>
      <rect x="60" y="155" width="294" height="8" fill="var(--magenta)"/>
      <rect x="0" y="166" width="420" height="2" fill="var(--navy)"/>
      <rect x="0" y="168" width="420" height="480" fill="url(#coastTone)" role="img" aria-label="Aerial photograph of a rocky coastal headland above turquoise water"/>
      <polygon points="230,520 290,490 420,546 420,610" fill="var(--white)"/>
      <polygon points="283,500 420,436 420,550" fill="var(--navy)"/>
      <polygon points="0,624 258,510 420,572 420,994 0,994" fill="var(--magenta)"/>
      <rect x="0" y="777" width="420" height="21" fill="var(--magenta-dark)"/>
    </svg>
    <div class="brand" style="top:18px">
      <div class="brand__mark"></div>
      <div class="brand__name">CASCADIA LABOR<br>ALLIANCE</div>
    </div>
    <div class="message" style="top:629px">
      <div class="kicker">OREGON'S WORKFORCE SYSTEM</div>
      <div class="headline" style="font-size:45px;margin-top:10px">ENSURES ALL</div>
      <div class="subline" style="font-size:27px;margin-top:6px">OREGONIANS POSSESS<br>THE TALENT NEEDED</div>
      <div class="tagband" style="margin-top:1px">FOR COMMUNITIES TO THRIVE AND PROSPER.</div>
    </div>
    <div class="url" style="top:932px">cascadialaboralliance.example</div>
  </section>

  <!-- Banner: leadership message -->
  <section class="banner banner--leadership">
    <svg class="shapes" width="420" height="994" viewBox="0 0 420 994">
      <defs>
        <linearGradient id="firTone" x1="0" y1="0" x2="1" y2="1">
          <stop offset="0" stop-color="var(--fir)"/>
          <stop offset="0.5" stop-color="#8a6a3a"/>
          <stop offset="0.6" stop-color="var(--fir)"/>
          <stop offset="1" stop-color="var(--fir-dark)"/>
        </linearGradient>
      </defs>
      <rect x="62" y="167" width="293" height="8" fill="var(--navy)"/>
      <rect x="0" y="178" width="420" height="2" fill="var(--magenta)"/>
      <rect x="0" y="180" width="420" height="480" fill="url(#firTone)" role="img" aria-label="Close-up photograph of a Douglas fir cone hanging among green needles"/>
      <polygon points="0,448 132,516 0,560" fill="var(--magenta)"/>
      <polygon points="0,560 132,516 157,520 0,584" fill="var(--white)"/>
      <polygon points="0,584 157,520 420,632 420,994 0,994" fill="var(--navy)"/>
      <rect x="0" y="808" width="420" height="21" fill="var(--navy-dark)"/>
    </svg>
    <div class="brand" style="top:30px">
      <div class="brand__mark"></div>
      <div class="brand__name">CASCADIA LABOR<br>ALLIANCE</div>
    </div>
    <div class="message" style="top:635px">
      <div class="kicker">PROVIDING</div>
      <div class="headline" style="font-size:50px;margin-top:6px">LEADERSHIP</div>
      <div class="subline" style="font-size:36px;line-height:1.17;margin-top:6px">THAT PROMOTES<br>AND ADVANCES</div>
      <div class="tagband" style="font-size:15px;letter-spacing:2px;margin-top:2px">OREGON'S WORKFORCE SYSTEM.</div>
    </div>
    <div class="url" style="top:943px">cascadialaboralliance.example</div>
  </section>

</div>
</body>
</html>
```